Flyerdesign for a Sports Homepage

I need a design for our Merchandise/Discount Flyer.
we are going to sell high class sports equipment.
the flyer should be in Size A5 or between A5 and A4.
there should be mentioned our Product names:
Product name for powerlifting: Torvik
Product name for Boxing: ZL Boxing
Product name for Martial Arts: Murelt
Product name for MMA: PitVolt
Product name for Bodybuilding: Bramfold

our Storename: PushAndDuel
Homepage: www.pushandduel.example

there should be space for entering a discount code
shop logo and brand logos: all pictures are attached.

out of the box thinking is welcome

Target Market(s)

People who do powersports like powerlifting or mma

Industry/Entity Type

Sport

Requirements
Must have
• 2 sides, all our brandnames, homepage, shop name and sports

```html
<!DOCTYPE html>
<html lang="en">
<head>
<meta charset="UTF-8">
<title>PushAndDuel Flyer – Front and Back</title>
<link rel="stylesheet" href="https://fonts.googleapis.com/css2?family=Montserrat:wght@400;500;600;700;800;900&display=swap">
<style>
  :root {
    --bg: #d9d9d9;
    --flyer: #140606;
    --flyer-deep: #0a0303;
    --red: #e0201b;
    --red-dark: #7a0d0a;
    --ember: #ff5a1f;
    --white: #ffffff;
    --muted: #c9b9b6;
    --gold: #c9a24a;
  }
  * { box-sizing: border-box; margin: 0; padding: 0; }
  html, body { width: 841px; height: 1200px; overflow: hidden; }
  body {
    background: var(--bg);
    font-family: "Montserrat", sans-serif;
    display: flex;
    align-items: center;
    justify-content: center;
    gap: 15px;
  }
  .flyer {
    width: 405px;
    height: 573px;
    position: relative;
    overflow: hidden;
    background: radial-gradient(ellipse at 50% 30%, #3a0a06 0%, var(--flyer) 55%, var(--flyer-deep) 100%);
    color: var(--white);
    box-shadow: 0 6px 18px rgba(0,0,0,.35);
  }

  /* Front */
  .brand {
    position: absolute; top: 18px; left: 0; right: 0;
    display: flex; align-items: center; justify-content: center; gap: 7px;
    z-index: 2;
  }
  .brand-square { width: 16px; height: 16px; background: var(--gold); }
  .brand-name { font-weight: 700; font-size: 12px; letter-spacing: .5px; color: var(--white); }
  .hero-photo {
    position: absolute; top: 40px; left: 0; right: 0; height: 280px;
    background:
      radial-gradient(ellipse at 50% 55%, rgba(255,90,31,.55) 0%, rgba(160,20,10,.45) 40%, rgba(20,6,6,0) 72%),
      radial-gradient(ellipse at 20% 40%, rgba(224,32,27,.35) 0%, rgba(20,6,6,0) 50%),
      radial-gradient(ellipse at 80% 40%, rgba(224,32,27,.35) 0%, rgba(20,6,6,0) 50%);
  }
  .headline { position: absolute; top: 300px; left: 0; right: 0; text-align: center; }
  .headline-main {
    font-weight: 900; font-size: 50px; line-height: 1; color: var(--red); letter-spacing: 1px;
  }
  .headline-sub { font-weight: 700; font-size: 17px; letter-spacing: 3px; margin-top: 4px; }
  .headline-for { font-weight: 600; font-size: 7px; letter-spacing: 2px; margin-top: 3px; color: var(--muted); }
  .headline-sports { font-weight: 800; font-size: 16px; color: var(--red); letter-spacing: 1.5px; margin-top: 2px; }
  .intro {
    position: absolute; top: 418px; left: 60px; right: 60px;
    font-size: 7.5px; line-height: 1.5; text-align: center; color: var(--muted);
  }
  .offer {
    position: absolute; top: 460px; left: 34px; right: 34px;
    display: flex; align-items: center; gap: 10px;
  }
  .offer-value { font-weight: 900; font-size: 26px; line-height: .9; color: var(--white); }
  .offer-value small { display: block; font-size: 13px; font-weight: 800; color: var(--red); letter-spacing: 1px; }
  .offer-divider { width: 2px; height: 40px; background: var(--red); }
  .offer-text { font-weight: 700; font-size: 11px; line-height: 1.25; }
  .coupon-code {
    display: inline-block; margin-top: 4px; padding: 3px 12px;
    background: var(--red); font-weight: 800; font-size: 12px; letter-spacing: 2px;
  }
  .footer {
    position: absolute; bottom: 0; left: 0; right: 0; height: 30px;
    border-top: 1px solid var(--red-dark);
    display: flex; align-items: center; justify-content: center; gap: 6px;
    font-size: 8px; color: var(--muted);
  }
  .footer strong { color: var(--white); font-weight: 700; font-size: 9px; }

  /* Back */
  .collections-title {
    position: absolute; top: 24px; left: 0; right: 0; text-align: center;
    font-weight: 800; font-size: 24px; letter-spacing: 1px;
  }
  .collections-title span { color: var(--red); }
  .collection-list {
    position: absolute; top: 70px; left: 18px; right: 18px;
    display: flex; flex-direction: column; gap: 9px;
  }
  .collection {
    height: 85px; display: flex; align-items: center; gap: 10px;
    border-bottom: 1px solid rgba(224,32,27,.35);
    position: relative;
  }
  .collection:last-child { border-bottom: none; }
  .brand-emblem {
    width: 44px; height: 52px; flex: none;
    background: radial-gradient(circle at 50% 45%, var(--ember) 0%, var(--red) 45%, var(--red-dark) 100%);
    border-radius: 4px;
  }
  .collection-info { width: 150px; flex: none; }
  .collection-name { font-weight: 800; font-size: 11px; color: var(--red); letter-spacing: .5px; }
  .collection-desc { font-size: 7.5px; line-height: 1.45; color: var(--muted); margin-top: 3px; }
  .product-photo {
    width: 118px; height: 64px; flex: none; border-radius: 3px;
    background: radial-gradient(ellipse at 50% 55%, #4a4a4a 0%, #222 55%, rgba(20,6,6,0) 100%);
  }
  .price-tag {
    position: absolute; right: 0; top: 50%; transform: translateY(-50%);
    width: 42px; height: 42px; border-radius: 50%;
    background: var(--red); display: flex; align-items: center; justify-content: center;
    font-weight: 800; font-size: 9px;
  }
</style>
</head>
<body>

  <section class="flyer flyer-front">
    <div class="brand">
      <div class="brand-square"></div>
      <div class="brand-name">PushAndDuel</div>
    </div>
    <div class="hero-photo" role="img" aria-label="Boxers and lifters in red gloves posing in front of flames"></div>
    <div class="headline">
      <div class="headline-main">PREMIUM</div>
      <div class="headline-sub">QUALITY PRODUCTS</div>
      <div class="headline-for">FOR ALL</div>
      <div class="headline-sports">LIFTING &amp; FIGHTING SPORTS</div>
    </div>
    <p class="intro">We focus on customer support and getting our products shipped quickly so you can start training the moment they arrive.</p>
    <div class="offer">
      <div class="offer-value">15%<small>OFF</small></div>
      <div class="offer-divider"></div>
      <div class="offer-text">ON FIRST ORDER WITH<br>COUPON CODE<br><span class="coupon-code">PD25</span></div>
    </div>
    <div class="footer">Visit to know more at: <strong>www.pushandduel.example</strong></div>
  </section>

  <section class="flyer flyer-back">
    <h2 class="collections-title">OUR <span>COLLECTIONS</span></h2>
    <div class="collection-list">
      <div class="collection">
        <div class="brand-emblem" role="img" aria-label="Torvik brand emblem"></div>
        <div class="collection-info">
          <div class="collection-name">POWER LIFTING</div>
          <div class="collection-desc">Torvik: Belts, straps and wrist wraps built for heavy lifts.</div>
        </div>
        <div class="product-photo" role="img" aria-label="Lifting belt and wrist wraps"></div>
        <div class="price-tag">$15.00</div>
      </div>
      <div class="collection">
        <div class="brand-emblem" role="img" aria-label="ZL Boxing brand emblem"></div>
        <div class="collection-info">
          <div class="collection-name">ZL BOXING</div>
          <div class="collection-desc">Gloves, pads and hand wraps for every round.</div>
        </div>
        <div class="product-photo" role="img" aria-label="Boxing gloves"></div>
        <div class="price-tag">$15.00</div>
      </div>
      <div class="collection">
        <div class="brand-emblem" role="img" aria-label="PitVolt brand emblem"></div>
        <div class="collection-info">
          <div class="collection-name">PITVOLT MMA</div>
          <div class="collection-desc">Fight gloves, shorts and guards for cage work.</div>
        </div>
        <div class="product-photo" role="img" aria-label="MMA gloves and shin guards"></div>
        <div class="price-tag">$15.00</div>
      </div>
      <div class="collection">
        <div class="brand-emblem" role="img" aria-label="Bramfold brand emblem"></div>
        <div class="collection-info">
          <div class="collection-name">BRAMFOLD BODYBUILDING</div>
          <div class="collection-desc">Grips, shakers and apparel for daily gym sessions.</div>
        </div>
        <div class="product-photo" role="img" aria-label="Gym shaker and grips"></div>
        <div class="price-tag">$15.00</div>
      </div>
      <div class="collection">
        <div class="brand-emblem" role="img" aria-label="Murelt brand emblem"></div>
        <div class="collection-info">
          <div class="collection-name">MURELT MARTIAL ARTS</div>
          <div class="collection-desc">Belts, uniforms and mitts for dojo training.</div>
        </div>
        <div class="product-photo" role="img" aria-label="Martial arts mitts"></div>
        <div class="price-tag">$15.00</div>
      </div>
    </div>
    <div class="footer">Visit to know more at: <strong>www.pushandduel.example</strong></div>
  </section>

</body>
</html>
```